Spaceman/ Astronaut Graffiti Full Sleeve

I want a full length sleeve for the right arm, starting from the top of the shoulder to the wrist bone. The basic idea is to have a bunch of little astronauts floating around in "space" with spray paint cans doing graffiti and creating planets, and other things. Also some random space men just doing odd activities and I will include examples in the upload. Lastly, I would like the quote "Live out of your imagination, not your history", starting at the top of the sleeve going to the bottom with each word separate and being painted by 1 or more little astronauts and the words to be in a neon graffiti style. It is definitely a lot and I'm obviously willing to pay for a design that reflects my ideals. I love vibrant colors and want the sleeve to reflect as such. Also, id like one of them to have a net trying to catch a jellyfish, Idk why but I want a jelly in there. I do prefer realism on the astronauts and other items. Ive included the style(s) of graffiti I'd like to have the quote be written in and also some ideas of little space men perspective wise and maybe some of the weird things they would be doing.

I've updated the pictures. In the last one, it shows a relative color scheme/ layout idea and the placement of how how I would like the words trailing down my arm. Maybe this was a little unclear at first.

Thank you in advance for all your time and effort!!

• Grafitti style

```html
<!DOCTYPE html>
<html lang="en">
<head>
<meta charset="utf-8">
<title>Live Out Of Your Imagination – Sleeve Layout</title>
<link rel="stylesheet" href="https://fonts.googleapis.com/css2?family=Anton&display=swap">
<style>
  :root {
    --page: #ffffff;
    --band-teal: #13a596;
    --band-blue: #0a6db8;
    --band-green: #0aa94e;
    --ink: #0d0d0d;
    --red: #e2262b;
    --violet: #9a2f94;
    --lime: #e3ef1d;
    --leaf: #0d9b3e;
    --amber: #f9a51a;
    --flame: #e8381f;
    --splash-orange: #f39a1d;
    --splash-yellow: #fbc531;
    --splash-pink: #f2a7a0;
    --splash-purple: #8b3a8f;
    --figure-light: #e9eef3;
  }
  html, body {
    margin: 0;
    padding: 0;
    width: 1200px;
    height: 848px;
    overflow: hidden;
    background: var(--page);
  }
  .canvas {
    position: relative;
    width: 1200px;
    height: 848px;
  }
  .sleeve-band {
    position: absolute;
    left: 0;
    top: 294px;
    width: 1200px;
    height: 260px;
    background: linear-gradient(90deg, var(--band-teal) 0%, var(--band-blue) 50%, var(--band-green) 100%);
  }
  .artwork {
    position: absolute;
    left: 0;
    top: 0;
    width: 1200px;
    height: 848px;
  }
  .quote {
    font-family: "Anton", "Impact", sans-serif;
    stroke: var(--ink);
    stroke-linejoin: miter;
    paint-order: stroke fill;
  }
  .quote-outline {
    fill: var(--ink);
    stroke: var(--ink);
    stroke-width: 12px;
    stroke-linejoin: round;
  }
  .quote-face {
    stroke-width: 2px;
  }
</style>
</head>
<body>
<main class="canvas">
  <div class="sleeve-band"></div>

  <svg class="artwork" width="1200" height="848" viewBox="0 0 1200 848" xmlns="http://www.w3.org/2000/svg">
    <defs>
      <linearGradient id="grad-live" x1="0" y1="0" x2="0" y2="1">
        <stop offset="0" stop-color="var(--red)"/>
        <stop offset="0.45" stop-color="var(--violet)"/>
        <stop offset="0.8" stop-color="var(--red)"/>
      </linearGradient>
      <linearGradient id="grad-imagination" x1="0" y1="0" x2="0" y2="1">
        <stop offset="0.1" stop-color="var(--lime)"/>
        <stop offset="0.85" stop-color="var(--leaf)"/>
      </linearGradient>
      <linearGradient id="grad-history" x1="0" y1="0" x2="0" y2="1">
        <stop offset="0.05" stop-color="var(--flame)"/>
        <stop offset="0.7" stop-color="var(--amber)"/>
      </linearGradient>
      <radialGradient id="splash-warm" cx="0.5" cy="0.5" r="0.6">
        <stop offset="0" stop-color="var(--splash-yellow)"/>
        <stop offset="1" stop-color="var(--splash-orange)"/>
      </radialGradient>

      <filter id="rough-paint" x="-20%" y="-20%" width="140%" height="140%">
        <feTurbulence type="fractalNoise" baseFrequency="0.09" numOctaves="2" seed="4" result="noise"/>
        <feDisplacementMap in="SourceGraphic" in2="noise" scale="7" xChannelSelector="R" yChannelSelector="G"/>
      </filter>
      <filter id="rough-letter" x="-5%" y="-10%" width="110%" height="120%">
        <feTurbulence type="fractalNoise" baseFrequency="0.05" numOctaves="1" seed="2" result="noise"/>
        <feDisplacementMap in="SourceGraphic" in2="noise" scale="2.5" xChannelSelector="R" yChannelSelector="G"/>
      </filter>

      <g id="splat">
        <path d="M-22,-4 C-27,-18 -8,-27 2,-19 C11,-31 25,-20 20,-7 C33,-2 27,17 12,14 C8,27 -10,25 -12,14 C-27,17 -31,4 -22,-4Z"/>
        <circle cx="-34" cy="-14" r="3"/>
        <circle cx="31" cy="-22" r="2.5"/>
        <circle cx="38" cy="8" r="2"/>
        <circle cx="-30" cy="20" r="2.5"/>
        <circle cx="4" cy="-36" r="2"/>
        <circle cx="20" cy="30" r="1.8"/>
        <circle cx="-44" cy="2" r="1.6"/>
      </g>

      <path id="arc-imagination" d="M 358 396 Q 572 262 788 400"/>
    </defs>

    <g class="paint-splashes" filter="url(#rough-paint)" role="img" aria-label="Spray paint splatters behind the lettering">
      <use href="#splat" fill="url(#splash-warm)" transform="translate(72 476) scale(1.2)"/>
      <use href="#splat" fill="var(--splash-purple)" opacity="0.85" transform="translate(250 468) scale(1.05) rotate(40)"/>
      <use href="#splat" fill="url(#splash-warm)" transform="translate(376 336) scale(1.1) rotate(-20)"/>
      <use href="#splat" fill="var(--splash-pink)" opacity="0.8" transform="translate(598 350) scale(0.8) rotate(70)"/>
      <use href="#splat" fill="url(#splash-warm)" transform="translate(590 356) scale(0.55)"/>
      <use href="#splat" fill="var(--splash-pink)" opacity="0.75" transform="translate(668 322) scale(0.6) rotate(15)"/>
      <use href="#splat" fill="var(--splash-purple)" opacity="0.85" transform="translate(752 340) scale(0.9) rotate(110)"/>
      <use href="#splat" fill="url(#splash-warm)" transform="translate(768 472) scale(1.05) rotate(30)"/>
      <use href="#splat" fill="var(--splash-purple)" opacity="0.85" transform="translate(1128 470) scale(1.05) rotate(-30)"/>
    </g>

    <rect class="figure-left" x="78" y="303" width="136" height="153" rx="30"
          fill="var(--band-teal)" opacity="0.55" role="img"
          aria-label="Line drawing of an astronaut reaching up to a sparkling star"/>
    <rect class="figure-center" x="420" y="388" width="193" height="166" rx="40"
          fill="var(--figure-light)" opacity="0.9" role="img"
          aria-label="Line drawing of an astronaut in a white spacesuit waving"/>
    <rect class="figure-right" x="887" y="296" width="193" height="142" rx="36"
          fill="var(--figure-light)" opacity="0.75" role="img"
          aria-label="Line drawing of an astronaut floating on his back with a small cloud"/>

    <g class="quote-block quote-live" filter="url(#rough-letter)">
      <text class="quote quote-outline" x="40" y="538" font-size="90"
            textLength="266" lengthAdjust="spacingAndGlyphs"
            rotate="-4 3 -3 2 0 -3 3 -2 0 4 -3">LIVE OUT OF</text>
      <text class="quote quote-face" x="40" y="538" font-size="90"
            textLength="266" lengthAdjust="spacingAndGlyphs"
            rotate="-4 3 -3 2 0 -3 3 -2 0 4 -3"
            fill="url(#grad-live)">LIVE OUT OF</text>
    </g>

    <g class="quote-block quote-imagination" filter="url(#rough-letter)">
      <text class="quote quote-outline" font-size="52">
        <textPath href="#arc-imagination" textLength="452"
                  lengthAdjust="spacingAndGlyphs">YOUR IMAGINATION</textPath>
      </text>
      <text class="quote quote-face" font-size="52" fill="url(#grad-imagination)">
        <textPath href="#arc-imagination" textLength="452"
                  lengthAdjust="spacingAndGlyphs">YOUR IMAGINATION</textPath>
      </text>
    </g>

    <g class="quote-block quote-history" filter="url(#rough-letter)">
      <text class="quote quote-outline" x="748" y="538" font-size="90"
            textLength="414" lengthAdjust="spacingAndGlyphs"
            rotate="-3 2 -2 0 3 -2 2 -3 0 -2 3 -2 2 -3 2 -2">NOT YOUR HISTORY</text>
      <text class="quote quote-face" x="748" y="538" font-size="90"
            textLength="414" lengthAdjust="spacingAndGlyphs"
            rotate="-3 2 -2 0 3 -2 2 -3 0 -2 3 -2 2 -3 2 -2"
            fill="url(#grad-history)">NOT YOUR HISTORY</text>
    </g>
  </svg>
</main>
</body>
</html>
```